Rewards Postcard

We are a women's apparel store in Illinois and Iowa and we have a rewards program, we send rewards postcards - but the ones we send are not very good and don't really convey a nice sense of a true thank you, it currently looks just like a coupon postcard. I would really like the customer know that it is a reward. I am going to attach several examples of our previous things we have done - I will make a note on what we like or don't like.

Target Market(s)

existing cusotmers

Industry/Entity Type

Womens Clothing

```html
<!DOCTYPE html>
<html lang="en">
<head>
<meta charset="utf-8">
<title>Willow Lane Rewards Postcard</title>
<link rel="stylesheet" href="https://fonts.googleapis.com/css2?family=Libre+Baskerville&family=Open+Sans:wght@400;700&family=Arimo&display=swap">
<style>
  :root {
    --card-purple: #6a5b8f;
    --card-purple-light: #74659a;
    --ink-white: #ffffff;
    --ink-soft: #f1eef7;
  }
  html, body {
    margin: 0;
    padding: 0;
    width: 1200px;
    height: 930px;
    overflow: hidden;
  }
  .postcard {
    position: relative;
    width: 1200px;
    height: 930px;
    background: radial-gradient(ellipse at 50% 45%, var(--card-purple-light), var(--card-purple) 70%);
    color: var(--ink-white);
    overflow: hidden;
  }
  .headline {
    position: absolute;
    left: 50px;
    top: 118px;
    margin: 0;
    font-family: "Libre Baskerville", serif;
    font-weight: 400;
    font-size: 78px;
    line-height: 126px;
    letter-spacing: -1px;
  }
  .headline span { display: block; }
  .benefits {
    position: absolute;
    left: 619px;
    top: 104px;
    width: 548px;
  }
  .benefit-title {
    margin: 0;
    font-family: "Libre Baskerville", serif;
    font-weight: 400;
    font-size: 27px;
    line-height: 40px;
  }
  .benefit-text {
    margin: 0;
    font-family: "Arimo", Arial, sans-serif;
    font-size: 18.5px;
    line-height: 25.5px;
  }
  .points .benefit-text { margin-top: 30px; }
  .perks { margin-top: 28px; }
  .perks .benefit-text { margin-top: 28px; }
  .rewards { margin-top: 26px; }
  .rewards .benefit-text { margin-top: 22px; }
  .tagline {
    position: absolute;
    left: 619px;
    width: 514px;
    top: 712px;
    margin: 0;
    text-align: center;
    font-family: "Open Sans", sans-serif;
    font-weight: 700;
    font-size: 18px;
    line-height: 28px;
    text-transform: uppercase;
  }
  .more-info {
    position: absolute;
    left: 619px;
    width: 514px;
    top: 784px;
    margin: 0;
    text-align: center;
    font-family: "Libre Baskerville", serif;
    font-size: 14px;
    color: var(--ink-soft);
  }
  .more-info .web-address {
    font-family: "Open Sans", sans-serif;
    font-size: 15px;
    color: var(--ink-white);
  }
</style>
</head>
<body>
<main class="postcard">
  <h1 class="headline">
    <span>Now</span>
    <span>Willow Lane</span>
    <span>Offers you</span>
    <span>Even more.</span>
  </h1>

  <section class="benefits">
    <div class="benefit points">
      <h2 class="benefit-title">More points.</h2>
      <p class="benefit-text">You already get 10 points for every dollar you spend at Willow Lane direct stores and willowlanedirect.com Plus, now through Dec. 24, you can earn 300 Bonus Pints when you buy 3 or more Willow Lane direct cards and 100 Bonus Points for each Willow Lane direct Keepshae Ornament you buy.</p>
    </div>
    <div class="benefit perks">
      <h2 class="benefit-title">More perks.</h2>
      <p class="benefit-text">Look for more suprise offers and coupons like this one-just for shopping with us throughout the year.</p>
    </div>
    <div class="benefit rewards">
      <h2 class="benefit-title">More rewards.</h2>
      <p class="benefit-text">Once you hit 2.500 points, you’ll become a Platium member. That means you earn even more Rewards Dollars you can use to buy things you love at Willow Lane direct stores and WillowLanedirect.com</p>
    </div>
  </section>

  <p class="tagline">It all adds up to a more rewarding<br>experience for members like you.</p>
  <p class="more-info">Find out more at <span class="web-address">Willowlanedirect.com/Willowlanerewards</span></p>
</main>
</body>
</html>
```